依頼詳細
基礎化粧品シリーズのパッケージデザイン(外箱)
絵柄等はシリーズ全体で統一し、全体又はポイントで色味を変えて差別化したいと思っています。
化粧品本体のデザインは既に決定しており、容器は全体的にホワイトベースで、商品名の下にツノマタのワンポイントイラストが入ったシンプルなデザインになっています。(ワンポイントイラストのカラーは外箱デザイン決定後に、統一性のある色に決めようと思っています。)
中身がシンプルなので、外箱は目を引くようなデザインをと考えていますが、あまり派手すぎないものがいいです。
記載項目
W40×D32×H150mm
材質はまだ確定していません。
希望イメージ
シンプル 複雑
単色 カラフル
暗い 明るい
日常 高級
遊び心 厳粛
未来的 伝統的
女性的 男性的
希望する色
イメージしている色「海藻→青紫、赤紫系」「海、波→青緑系」
納品ファイル
• 高解像度JPG (.jpg)

```html
<!DOCTYPE html>
<html lang="en">
<head>
<meta charset="UTF-8">
<title>ONDA BELLE – Cleansing cream carton</title>
<link href="https://fonts.googleapis.com/css2?family=Tinos&family=Noto+Sans+JP:wght@500&display=swap" rel="stylesheet">
<style>
  :root {
    --magenta: #d23f93;
    --orchid: #a23a9a;
    --violet: #5a2f8c;
    --navy: #1d2472;
    --deep-navy: #141a5e;
    --white: #ffffff;
    --panel-line: rgba(255,255,255,0.55);
    --faint: rgba(255,255,255,0.16);
    --pill: #3f5bd0;
    --flap-top: #e27ab6;
  }
  * { margin: 0; padding: 0; box-sizing: border-box; }
  html, body { width: 694px; height: 1200px; overflow: hidden; background: #ffffff; }
  .carton {
    position: relative;
    width: 694px;
    height: 1200px;
    font-family: "Tinos", "Times New Roman", serif;
    color: var(--white);
  }
  .top-flap {
    position: absolute;
    left: 213px; top: 0;
    width: 268px; height: 132px;
    background: linear-gradient(180deg, var(--flap-top) 0%, var(--magenta) 40%, var(--orchid) 100%);
    border: 1px solid var(--panel-line);
    display: flex; flex-direction: column; align-items: center; justify-content: flex-end;
    padding-bottom: 20px;
  }
  .top-flap .flap-name {
    font-size: 34px; line-height: 1.02; text-align: center; letter-spacing: 1px;
  }
  .body {
    position: absolute;
    left: 0; top: 132px;
    width: 694px; height: 1068px;
    background: linear-gradient(180deg, var(--magenta) 0%, var(--orchid) 30%, var(--violet) 62%, var(--navy) 85%, var(--deep-navy) 100%);
    overflow: hidden;
  }
  .panel {
    position: absolute; top: 0; height: 100%;
    border-left: 1px solid var(--panel-line);
    border-right: 1px solid var(--panel-line);
  }
  .panel-left { left: 0; width: 213px; }
  .panel-front { left: 213px; width: 268px; }
  .panel-right { left: 481px; width: 213px; }
  .side-name {
    position: absolute; top: 90px; left: 50%; transform: translateX(-50%);
    display: flex; flex-direction: column; align-items: center;
    font-size: 34px; line-height: 1; gap: 35px;
  }
  .side-name .gap { height: 40px; }
  .front-watermark {
    position: absolute; left: 6px; top: 20px;
    writing-mode: vertical-rl;
    font-size: 92px; letter-spacing: 6px; line-height: 1;
    color: var(--faint);
    white-space: nowrap;
  }
  .brand-block {
    position: absolute; left: 40px; top: 280px; width: 210px;
  }
  .brand-mark {
    width: 16px; height: 16px; border-radius: 50%;
    background: #c9a24a; margin-bottom: 16px; margin-left: 4px;
  }
  .brand-name { font-size: 46px; line-height: 1.05; letter-spacing: 0.5px; }
  .brand-story {
    margin-top: 14px; font-size: 15px; line-height: 1.22; width: 190px;
  }
  .product-type {
    position: absolute; left: 40px; top: 820px;
  }
  .product-type .en { font-size: 24px; }
  .product-type .jp {
    display: inline-block; margin-top: 8px;
    background: var(--pill); border-radius: 10px;
    padding: 2px 12px;
    font-family: "Noto Sans JP", sans-serif; font-size: 13px; font-weight: 500;
  }
  .maker {
    position: absolute; left: 0; width: 100%; top: 995px;
    text-align: center; font-size: 15px; letter-spacing: 1px;
  }
  .wave-area {
    position: absolute; left: 300px; top: 760px; width: 394px; height: 220px;
    background: radial-gradient(ellipse at 60% 60%, rgba(90,140,230,0.28), rgba(60,90,200,0.0) 70%);
  }
  .kelp-area {
    position: absolute; left: 481px; top: 120px; width: 213px; height: 560px;
    background: radial-gradient(ellipse at 70% 50%, rgba(255,255,255,0.07), rgba(255,255,255,0) 70%);
  }
</style>
</head>
<body>
<div class="carton">
  <div class="top-flap">
    <div class="flap-name">ONDA<br>BELLE</div>
  </div>

  <div class="body">
    <div class="kelp-area" role="img" aria-label="Faint seaweed silhouette decoration"></div>
    <div class="wave-area" role="img" aria-label="Flowing blue ocean wave line pattern"></div>

    <section class="panel panel-left">
      <div class="side-name">
        <span>O</span><span>N</span><span>D</span><span>A</span>
        <span class="gap"></span>
        <span>B</span><span>E</span><span>L</span><span>L</span><span>E</span>
      </div>
    </section>

    <section class="panel panel-front">
      <div class="front-watermark">ONDA BELLE</div>
      <div class="brand-block">
        <div class="brand-mark"></div>
        <div class="brand-name">ONDA<br>BELLE</div>
        <p class="brand-story">Beauty products from seaweed “TSUNOMATA” was born and nurtured choshi Ocean.</p>
      </div>
      <div class="product-type">
        <div class="en">Cleansing cream</div>
        <div class="jp">クレンジングクリーム</div>
      </div>
      <div class="maker">KAIRO MARINE LABO</div>
    </section>

    <section class="panel panel-right">
      <div class="side-name">
        <span>O</span><span>N</span><span>D</span><span>A</span>
        <span class="gap"></span>
        <span>B</span><span>E</span><span>L</span><span>L</span><span>E</span>
      </div>
    </section>
  </div>
</div>
</body>
</html>
```